Gobal construction supply company needs new business card design

I need a business card design for my global supply company using an existing logo. i will be looking to print these on rounded corner cards with the black background version of my logo on the back. on the front white background, my logo again and my simple details.

```html
<!DOCTYPE html>
<html lang="en">
<head>
<meta charset="utf-8">
<title>Meridian Build Supply – Business Card</title>
<link rel="stylesheet" href="https://fonts.googleapis.com/css2?family=Open+Sans:wght@400;600;700&display=swap">
<style>
  :root {
    --stage: #2b2b2b;
    --card-black: #141414;
    --card-white: #fbfbfb;
    --brand-red: #d8232a;
    --ink: #111111;
    --ink-soft: #3a3a3a;
    --mark-on-black: #3c3c3c;
  }
  * { margin: 0; padding: 0; box-sizing: border-box; }
  html, body {
    width: 1200px; height: 942px; overflow: hidden;
    background: var(--stage);
    font-family: "Open Sans", Arial, sans-serif;
  }
  .stage {
    width: 1200px; height: 942px;
    display: flex; align-items: center; justify-content: center; gap: 40px;
  }
  .card {
    width: 540px; height: 315px;
    border-radius: 26px;
    position: relative;
    overflow: hidden;
  }
  /* Back */
  .card--back {
    background: var(--card-black);
    display: flex; flex-direction: column; align-items: center; justify-content: center;
  }
  .brand {
    display: flex; align-items: center; gap: 12px;
  }
  .brand__name {
    font-weight: 700; letter-spacing: 0.5px; text-transform: uppercase;
  }
  .brand__dot {
    width: 16px; height: 16px; border-radius: 50%; background: var(--brand-red);
  }
  .card--back .brand__name { color: var(--mark-on-black); font-size: 26px; }
  .card--back .brand__dot { width: 22px; height: 22px; }
  .rule {
    width: 200px; height: 2px; background: var(--brand-red); margin: 18px 0;
  }
  .back__web {
    color: var(--brand-red); font-size: 16px; letter-spacing: 3px;
  }
  /* Front */
  .card--front {
    background: var(--card-white);
    display: flex; align-items: center;
    padding: 0 34px;
  }
  .front__brand {
    width: 210px;
    display: flex; flex-direction: column; align-items: flex-start;
  }
  .card--front .brand__name { color: var(--ink); font-size: 17px; line-height: 1.2; }
  .front__brand .rule { width: 170px; margin: 12px 0 0; }
  .divider {
    width: 2px; height: 170px; background: var(--brand-red); margin: 0 30px 0 8px;
  }
  .details { flex: 1; }
  .details__name { font-size: 30px; font-weight: 400; color: var(--ink); line-height: 1.1; }
  .details__title { font-size: 14px; color: var(--brand-red); margin: 4px 0 18px; }
  .contact { list-style: none; }
  .contact li {
    display: flex; align-items: center; gap: 10px;
    font-size: 14px; color: var(--ink-soft); margin-bottom: 8px;
  }
  .contact svg { width: 15px; height: 15px; flex: none; }
</style>
</head>
<body>
<main class="stage">
  <section class="card card--back" aria-label="Card back">
    <div class="brand">
      <span class="brand__name">Meridian Build Supply</span>
      <span class="brand__dot"></span>
    </div>
    <div class="rule"></div>
    <p class="back__web">www.yourwebsite.com</p>
  </section>

  <section class="card card--front" aria-label="Card front">
    <div class="front__brand">
      <div class="brand">
        <span class="brand__name">Meridian<br>Build Supply</span>
        <span class="brand__dot"></span>
      </div>
      <div class="rule"></div>
    </div>
    <div class="divider"></div>
    <div class="details">
      <h1 class="details__name">Your Name</h1>
      <p class="details__title">Job Title</p>
      <ul class="contact">
        <li>
          <svg viewBox="0 0 16 16" aria-hidden="true"><path fill="#d8232a" d="M4 1h3l1 4-2 1.5a9 9 0 0 0 3.5 3.5L11 8l4 1v3a2 2 0 0 1-2 2A12 12 0 0 1 2 3a2 2 0 0 1 2-2z"/></svg>
          000 000 0000
        </li>
        <li>
          <svg viewBox="0 0 16 16" aria-hidden="true"><rect x="1" y="3" width="14" height="10" rx="1" fill="#d8232a"/><path d="M1.5 3.5 8 9l6.5-5.5" fill="none" stroke="#fff" stroke-width="1.3"/></svg>
          youremail@xyz.com
        </li>
        <li>
          <svg viewBox="0 0 16 16" aria-hidden="true"><g fill="none" stroke="#d8232a" stroke-width="1.3"><circle cx="8" cy="8" r="6.5"/><ellipse cx="8" cy="8" rx="3" ry="6.5"/><path d="M1.5 8h13M2.5 5h11M2.5 11h11"/></g></svg>
          www.yourwebsite.com
        </li>
      </ul>
    </div>
  </section>
</main>
</body>
</html>
```